Medical practice in the United States needs a landing page

Our medical practice, based in Dallas, Texas, is called 'Talwick Headache Clinics.' We perform the Talwick Method on patients to treat chronic, severe head pain.

We currently have a landing page for our Chatterly ads, but we'd like to improve the page's design to increase the lead conversion rate. The landing page contains a form that allows people to register for our free, on-demand informational webinar about the procedure. Either part of the registration form or all of the registration form must be above the fold.

Here is the link to the landing page that needs a more attractive design: https://talwickheadache.example/migraine-treatment-webinars/talwick-treatment-free-patient-webinar/

Once a lead submits the registration form on that page, they are redirected to a different page on the site that contains the webinar video.

Here is a direct link to the page that contains the actual video (note: this is NOT the page for which I am requesting an improved design for this project; I am only including this link so that you can watch the video if you think it will help you create a design for the other page):

https://talwickheadache.example/talwick-headache-clinics-patient-information-webinar/
Updates

Designs look the same

Hello all,

The designs so far have been very impressive! Thank you all for your hard work. Please don't feel compelled to use my exact wording, though, for the description of the webinar. The only requirement is that the form on the page be present and contain the same form fields.

Thanks again!

Target Market(s)

Patients with chronic, severe head pain

Industry/Entity Type

Healthcare

Requirements
Must have
• Either part of the registration form or all of the registration form must be above the fold.
Should not have
• The registration form located completely below the fold.

```html
<!DOCTYPE html>
<html lang="en">
<head>
<meta charset="utf-8">
<title>Talwick Method Free Webinar Registration</title>
<link href="https://fonts.googleapis.com/css2?family=Figtree:wght@400;500;600;700&display=swap" rel="stylesheet">
<style>
:root{
  --teal:#0b4a63;
  --ink:#17262e;
  --muted:#5d6b72;
  --green:#7cc043;
  --green-soft:#eff6e6;
  --field:#f3f4f5;
  --band:#eef5f8;
  --line:#e4e7e9;
  --white:#ffffff;
}
*{box-sizing:border-box;margin:0;padding:0}
html,body{width:1200px;height:2408px;overflow:hidden;background:var(--white)}
body{font-family:"Figtree",sans-serif;color:var(--ink);position:relative}
.abs{position:absolute}
.logo{font-family:"Figtree",sans-serif;font-size:29px;font-weight:400;color:var(--teal);letter-spacing:-0.5px;display:flex;align-items:center;gap:10px}
.logo .dot{width:14px;height:14px;border-radius:50%;background:var(--green)}
.btn{position:absolute;height:43px;border-radius:4px;font-size:12px;font-weight:600;letter-spacing:.3px;display:flex;align-items:center;justify-content:center;text-transform:uppercase}
.btn-contact{background:var(--green-soft);color:var(--green);width:128px}
.btn-consult{background:var(--green);color:var(--white);width:174px}
.rule{left:83px;width:1034px;height:1px;background:var(--line);top:83px}
.nav{top:114px;left:0;width:1200px;display:flex;justify-content:center;gap:30px;font-size:14px;font-weight:500}
.nav span{display:flex;align-items:center;gap:8px}
.hero-photo{left:83px;top:165px;width:852px;height:786px;border-radius:8px;background:linear-gradient(135deg,#3f6f86 0%,#2f6479 45%,#29596e 100%)}
.card{left:437px;top:231px;width:680px;height:653px;background:var(--white);border-radius:8px;box-shadow:0 10px 40px rgba(0,0,0,.08);padding:33px}
.card h1{font-size:27px;font-weight:600;letter-spacing:-.2px;margin-bottom:32px}
.card h1 sup{font-size:14px}
.grid{display:grid;grid-template-columns:297px 297px;column-gap:20px;row-gap:16px}
.field label{display:block;font-size:13px;color:#3a474d;margin-bottom:6px}
.input{height:43px;background:var(--field);border-radius:4px;display:flex;align-items:center;justify-content:space-between;padding:0 14px;font-size:15px;color:#8a959a}
.note{font-size:11px;color:#4a565c;margin-top:8px;line-height:1.5}
.area{height:90px;align-items:flex-start;padding-top:14px}
.agree{display:flex;align-items:center;gap:12px;font-size:13.5px;margin-top:30px}
.check{width:20px;height:20px;border:1.5px solid var(--green);border-radius:3px;display:flex;align-items:center;justify-content:center}
.submit{margin-top:32px;height:43px;background:var(--teal);color:var(--white);border-radius:4px;font-size:11px;font-weight:600;display:flex;align-items:center;justify-content:center;letter-spacing:.3px}
.topics-title{top:1038px;width:1200px;text-align:center;font-size:28px;font-weight:600}
.topic{width:320px;text-align:center}
.topic .icon{width:47px;height:47px;border-radius:50%;background:var(--teal);margin:0 auto 26px;display:flex;align-items:center;justify-content:center}
.topic h3{font-size:15px;font-weight:600;letter-spacing:.2px;margin-bottom:8px}
.topic p{font-size:13.5px;line-height:20px;color:var(--muted)}
.band{left:83px;top:1598px;width:1033px;height:340px;background:var(--band);border-radius:20px}
.head-art{left:78px;top:1598px;width:104px;height:140px;border-radius:50px 50px 20px 20px;background:linear-gradient(180deg,#dce9ef,#eef5f8)}
.quote{left:166px;top:1685px;width:868px;height:166px;background:var(--white);border-radius:6px;text-align:center;padding:20px 22px 0}
.quote p{font-size:20.5px;line-height:27px;color:#4a565c}
.quote .who{margin-top:18px;font-size:18px;font-weight:600;color:var(--ink)}
.arrow{width:30px;height:54px;background:var(--white);top:1803px;display:flex;align-items:center;justify-content:center}
.arrow.left{left:83px;border-radius:0 27px 27px 0}
.arrow.right{left:1090px;border-radius:27px 0 0 27px}
.foot-addr{left:83px;top:2117px;font-size:13.5px;line-height:20px}
.foot-addr strong{font-weight:700}
.foot-col h4{font-size:15px;font-weight:600;margin-bottom:14px}
.foot-col a{display:block;font-size:13.5px;color:var(--muted);text-decoration:none;margin-bottom:18px}
</style>
</head>
<body>

<header>
  <div class="abs logo" style="left:83px;top:22px"><span class="dot"></span>Talwick Headache Clinics</div>
  <div class="btn btn-contact" style="left:795px;top:20px">Contact Us</div>
  <div class="btn btn-consult" style="left:942px;top:20px">Free Consultation</div>
  <div class="abs rule"></div>
  <nav class="abs nav">
    <span>Talwick Method® <svg width="11" height="7" viewBox="0 0 11 7"><path d="M1 1l4.5 4.5L10 1" fill="none" stroke="#17262e" stroke-width="1.6"/></svg></span>
    <span>About <svg width="11" height="7" viewBox="0 0 11 7"><path d="M1 1l4.5 4.5L10 1" fill="none" stroke="#17262e" stroke-width="1.6"/></svg></span>
    <span>Research <svg width="11" height="7" viewBox="0 0 11 7"><path d="M1 1l4.5 4.5L10 1" fill="none" stroke="#17262e" stroke-width="1.6"/></svg></span>
    <span>Patient Reviews <svg width="11" height="7" viewBox="0 0 11 7"><path d="M1 1l4.5 4.5L10 1" fill="none" stroke="#17262e" stroke-width="1.6"/></svg></span>
    <span>FAQ <svg width="11" height="7" viewBox="0 0 11 7"><path d="M1 1l4.5 4.5L10 1" fill="none" stroke="#17262e" stroke-width="1.6"/></svg></span>
    <span>Ask Our Patients</span>
    <span>Free Webinars</span>
  </nav>
</header>

<section>
  <div class="abs hero-photo" role="img" aria-label="Photo of a patient receiving care from a clinician, tinted in deep teal"></div>
  <form class="abs card">
    <h1>The Talwick Method<sup>®</sup> Free Webinar Registration</h1>
    <div class="grid">
      <div class="field"><label>First Name</label><div class="input">Enter First Name</div></div>
      <div class="field"><label>Last Name</label><div class="input">Enter Last Name</div></div>
      <div class="field"><label>Email</label><div class="input">Enter Email Address</div></div>
      <div class="field"><label>Phone Number</label><div class="input">Enter Phone Number</div></div>
      <div class="field"><label>Diagnosis</label><div class="input">Select <svg width="12" height="7" viewBox="0 0 12 7"><path d="M1 1l5 5 5-5" fill="none" stroke="#6b777c" stroke-width="1.5"/></svg></div>
        <div class="note">* Please select the one that best applies to you</div></div>
      <div class="field"><label>Insurance Carier</label><div class="input">Select <svg width="12" height="7" viewBox="0 0 12 7"><path d="M1 1l5 5 5-5" fill="none" stroke="#6b777c" stroke-width="1.5"/></svg></div>
        <div class="note">* Note: We do not accept Northway Health, StateCare, or Workers' Compensation.</div></div>
    </div>
    <div class="field" style="margin-top:16px"><label>Message (Optional)</label><div class="input area">Enter Additional Message</div></div>
    <div class="agree"><span class="check"><svg width="12" height="9" viewBox="0 0 12 9"><path d="M1 4.5l3.5 3.5L11 1" fill="none" stroke="#7cc043" stroke-width="1.6"/></svg></span>I agree with the site's User Agreement and Privacy Policy.</div>
    <div class="submit">VIEW WEBINAR NOW</div>
  </form>
</section>

<section>
  <h2 class="abs topics-title">Webinar Topics</h2>

  <div class="abs topic" style="left:86px;top:1124px">
    <div class="icon"><svg width="16" height="16" viewBox="0 0 16 16"><rect x="2" y="2" width="12" height="9" fill="#fff"/><path d="M5 9V7M8 9V5M11 9V6" stroke="#0b4a63" stroke-width="1.4"/><path d="M8 11v3M5 14l3-3 3 3" stroke="#fff" stroke-width="1.4" fill="none"/></svg></div>
    <h3>THE NUMBERS</h3>
    <p>The procedure’s compelling statistics: performed for over 25 years, more than 1000 patients, and a greater than 80% success rate!</p>
  </div>
  <div class="abs topic" style="left:440px;top:1124px">
    <div class="icon"><svg width="16" height="13" viewBox="0 0 16 13"><path d="M2 7l4 4 8-9" fill="none" stroke="#fff" stroke-width="2.6"/></svg></div>
    <h3>THE BENEFIT</h3>
    <p>Ability to test the stimulator to make sure it works for you. Medication-free migraine pain relief. Effectively treats intractable migraines.</p>
  </div>
  <div class="abs topic" style="left:793px;top:1124px">
    <div class="icon"><svg width="16" height="16" viewBox="0 0 16 16"><circle cx="8" cy="8" r="7.5" fill="#fff"/><text x="8" y="12" font-size="11" font-weight="700" text-anchor="middle" fill="#0b4a63" font-family="Figtree,sans-serif">?</text></svg></div>
    <h3>THE ANSWERS TO FAQS</h3>
    <p>How does the Talwick Method® work?<br>Am I a candidate for the procedure?<br>Is the procedure safe? And more!</p>
  </div>

  <div class="abs topic" style="left:86px;top:1351px">
    <div class="icon"><svg width="17" height="14" viewBox="0 0 17 14"><path d="M1 4h4l1.5-2.5h4L12 4h4v9H1z" fill="#fff"/><circle cx="8.5" cy="8.5" r="3" fill="#0b4a63"/><circle cx="8.5" cy="8.5" r="1.6" fill="#fff"/></svg></div>
    <h3>THE MEDIA</h3>
    <p>Video clips of the Talwick Method featured on The Clinic Hour, Channel 9 News, and Metro Network News.</p>
  </div>
  <div class="abs topic" style="left:440px;top:1351px">
    <div class="icon"><svg width="16" height="14" viewBox="0 0 16 14"><path d="M1 7h13M9 2l5 5-5 5" fill="none" stroke="#fff" stroke-width="2.2"/></svg></div>
    <h3>THE TREATMENT PROCESS</h3>
    <p>Details about the free initial consultation. The trial procedure vs. the permanent procedure. The treatment steps and timetable.</p>
  </div>
  <div class="abs topic" style="left:793px;top:1351px">
    <div class="icon"><svg width="16" height="16" viewBox="0 0 16 16"><rect x="1" y="7" width="3.5" height="8" fill="#fff"/><path d="M6 15V7l3-6c1.5 0 2 1 1.6 2.5L10 6h4c1 0 1.6 1 1.3 2l-1.6 5.5c-.3 1-1 1.5-2 1.5z" fill="#fff"/></svg></div>
    <h3>THE PATIENT STORIES</h3>
    <p>Many of our patients describe how the procedure changed their lives. Information about our patient ambassador program.</p>
  </div>
</section>

<section>
  <div class="abs band"></div>
  <div class="abs head-art" role="img" aria-label="Line illustration of a head in profile"></div>
  <blockquote class="abs quote">
    <p>“The best thing I’ve ever done. I have been in pain with migraines for five years. I had to quit my job and driving. Noise and lights were debilitating. Now I don’t hurt from the lights or loud noises. Thanks for the Talwick procedure!”</p>
    <div class="who">-Marla</div>
  </blockquote>
  <div class="abs arrow left"><svg width="8" height="13" viewBox="0 0 8 13"><path d="M7 1L2 6.5 7 12" fill="none" stroke="#17262e" stroke-width="1.8"/></svg></div>
  <div class="abs arrow right"><svg width="8" height="13" viewBox="0 0 8 13"><path d="M1 1l5 5.5L1 12" fill="none" stroke="#17262e" stroke-width="1.8"/></svg></div>
</section>

<footer>
  <div class="abs logo" style="left:83px;top:2020px"><span class="dot"></span>Talwick Headache Clinics</div>
  <div class="btn btn-contact" style="left:795px;top:2019px">Contact Us</div>
  <div class="btn btn-consult" style="left:942px;top:2019px">Free Consultation</div>

  <address class="abs foot-addr" style="font-style:normal">
    <strong>Talwick Headache Clinics</strong><br>
    Corporate Headquarters<br>
    4200 Larkspur Parkway<br>
    Suite 210<br>
    Dallas, Texas 75201<br><br>
    Main: (800) 555-0142<br>
    or (214) 555-0187<br>
    After Hours: (972) 555-0123<br>
    Fax: (855) 555-0199
  </address>

  <div class="abs foot-col" style="left:613px;top:2117px">
    <h4>WE OFFER</h4>
    <a>Free Webinar</a><a>Migraine Treatment</a><a>Talwick Method</a><a>Headache Help</a>
  </div>
  <div class="abs foot-col" style="left:878px;top:2117px">
    <h4>AT A GLANCE</h4>
    <a>Locations</a><a>Terms of Use</a><a>Privacy Policy</a><a>Sitemap</a>
  </div>
</footer>

</body>
</html>
```